Steady Harbor Leadership Roundtable Series Promotion

I'm wanting a single page (for now) website to promote my leadership training. Content would include: basic messaging what Steady Harbor means, invitation to join the Steady Harbor Roundtable workshops, have me come speak to them, join me on a leadership getaway, get personal coaching, watch some video links of Rud, then referrals of people saying nice things about Rud, connect to Rud’s personal website to learn more about me. The goal of the page is to 1) get people excited to attend a workshop, hear me speak, coach them, or join me on a getaway trip, 2) educate them in how they can get in control of their own life, and 3) link to my personal site to learn more about me. This is the general idea: https://www.perlwickstand.com/

Target Market(s)

Business owners or self improvement enthusiasts looking to take their businesses and personal lives to the next level.

Industry/Entity Type

Business Consultant

Coding

Coded - Design and coding required

Number of Pages Required

1 page

Font styles to use
Other font styles liked:
• See uploaded logo

Colors
0392cd

Requirements
Must have
• Fonts and colors that match the logo that was uploaded. Uplifting, inspirational look and feel.
Nice to have
• Similar to: https://www.perlwickstand.com/ and https://dorvankessling.com/

```html
<!DOCTYPE html>
<html lang="en">
<head>
<meta charset="utf-8">
<title>Rud Calloway – Leadership Consultant</title>
<link href="https://fonts.googleapis.com/css2?family=Poppins:wght@400;500;600;700;800&family=Roboto+Slab:wght@300;400&display=swap" rel="stylesheet">
<style>
:root{
  --orange:#f26a4b;
  --blue:#1d8fd6;
  --sky:#3db4ea;
  --navy:#2c4f9f;
  --amber:#f9a84c;
  --salmon:#f77c64;
  --ink:#1d1d2b;
  --grey:#8a8f98;
  --pale:#edf6fa;
  --footer:#0f2434;
  --white:#fff;
}
*{box-sizing:border-box;margin:0;padding:0}
html,body{width:1200px;height:4220px;overflow:hidden}
body{font-family:"Roboto Slab",Georgia,serif;color:var(--ink);background:var(--white);position:relative}
h1,h2,h3,h4,.sans{font-family:"Poppins",Arial,sans-serif}
.abs{position:absolute}
.ph{position:absolute}
.ring{position:absolute;border-radius:50%;border-style:solid;background:transparent}

/* hero */
.hero{position:absolute;top:0;left:0;width:1200px;height:660px;background:linear-gradient(90deg,var(--orange) 0 50%,var(--blue) 50% 100%);overflow:hidden}
.brand{position:absolute;left:56px;top:18px;display:flex;align-items:center;gap:8px;font-family:"Poppins",sans-serif;font-weight:700;font-size:15px;color:var(--white);letter-spacing:.5px}
.brand i{width:14px;height:14px;background:var(--white);display:block}
.nav{position:absolute;left:396px;top:38px;display:flex;gap:22px;font-family:"Poppins",sans-serif;font-weight:600;font-size:13px;color:var(--ink)}
.hero-word{position:absolute;left:0;width:1200px;text-align:center;font-family:"Poppins",sans-serif;font-weight:800;font-size:112px;line-height:1;color:rgba(40,26,56,.38);letter-spacing:2px}
.hero-photo{left:372px;top:120px;width:456px;height:540px;border-radius:180px 180px 0 0;background:linear-gradient(180deg,#c9ccd3 0%,#6f7785 55%,#23272f 100%)}

/* intro */
.intro-title{left:80px;top:770px;font-size:40px;font-weight:600;line-height:1.2}
.intro-text{left:80px;top:880px;width:440px;font-size:16px;line-height:1.6;color:var(--grey);font-weight:300}
.btn{position:absolute;font-family:"Poppins",sans-serif;font-size:13px;font-weight:500;border-radius:24px;display:flex;align-items:center;justify-content:center}
.btn-solid{background:var(--blue);color:var(--white)}
.btn-line{border:2px solid var(--blue);color:var(--ink)}
.stats{position:absolute;left:600px;top:772px;display:grid;grid-template-columns:240px 240px;gap:22px}
.stat{height:150px;color:var(--white);display:flex;flex-direction:column;align-items:center;justify-content:center;font-family:"Poppins",sans-serif}
.stat b{font-size:38px;font-weight:500;line-height:1.1}
.stat span{font-size:13px;margin-top:6px}

/* events */
.events{position:absolute;top:1200px;left:0;width:1200px;height:560px;background:var(--pale)}
.sec-title{position:absolute;font-size:40px;font-weight:600}
.arrows{position:absolute;display:flex;gap:14px}
.card{position:absolute;top:172px;width:248px}
.card .ph{position:relative;display:block;height:282px}
.date{position:absolute;right:10px;top:10px;width:54px;background:var(--white);text-align:center;font-family:"Poppins",sans-serif}
.date b{display:block;font-size:26px;font-weight:700;line-height:1.3}
.date span{display:block;background:var(--orange);color:var(--white);font-size:11px;font-weight:600}
.cap{margin-top:24px;display:flex;gap:14px;align-items:flex-start;font-family:"Poppins",sans-serif;font-size:15px;line-height:1.3}
.cap i{width:18px;height:2px;background:var(--orange);margin-top:10px;flex:none}

/* testimonials */
.quote{left:400px;top:1916px;width:700px;font-size:21px;line-height:1.55;color:var(--grey);font-weight:300}
.avatar{position:absolute;top:2262px;width:56px;height:56px;border-radius:50%}

/* vision */
.vision{position:absolute;top:2420px;left:0;width:1200px;height:660px;background:linear-gradient(90deg,var(--orange) 0 55%,var(--blue) 55% 100%);overflow:hidden}
.vision-word{position:absolute;right:0;font-family:"Poppins",sans-serif;font-weight:800;font-size:112px;line-height:1;color:rgba(40,26,56,.38)}
.vision-text{left:80px;top:220px;width:480px;color:var(--white);font-size:16px;line-height:1.6;font-weight:300}
.play{position:absolute;left:80px;top:478px;display:flex;align-items:center;gap:18px;color:var(--white);font-family:"Poppins",sans-serif;font-size:12px;font-weight:600;line-height:1.4}
.play i{width:60px;height:60px;border-radius:50%;background:var(--white);display:flex;align-items:center;justify-content:center}

/* news */
.news-card{position:absolute;top:3196px;width:352px}
.news-card .ph{position:relative;display:block;height:244px}
.news-meta{display:flex;gap:22px;margin-top:36px}
.news-day{font-family:"Poppins",sans-serif;text-align:center}
.news-day b{display:block;font-size:26px;font-weight:500}
.news-day span{font-size:10px;color:var(--grey)}
.news-tag{font-family:"Poppins",sans-serif;font-size:9px;font-weight:700;color:var(--orange);letter-spacing:.5px}
.news-title{font-family:"Poppins",sans-serif;font-size:15px;font-weight:500;line-height:1.35;margin-top:6px}

/* newsletter */
.newsletter{position:absolute;top:3740px;left:0;width:1200px;height:220px;background:var(--blue);color:var(--white)}
.field{position:absolute;left:570px;top:82px;width:550px;height:56px;background:var(--white);border-radius:30px;font-size:13px;color:#b0b4ba;padding:0 28px;display:flex;align-items:center;font-family:"Poppins",sans-serif}
.subscribe{position:absolute;right:4px;top:4px;width:170px;height:48px;border-radius:26px;background:var(--orange);color:var(--white);display:flex;align-items:center;justify-content:center;font-size:15px;font-weight:500}

/* footer */
.footer{position:absolute;top:3960px;left:0;width:1200px;height:260px;background:var(--footer);color:#c4ccd4}
.fcol{position:absolute;top:54px;font-size:13px;line-height:1.7}
.fcol h4{color:var(--white);font-size:16px;font-weight:600;margin-bottom:12px}
.fcol .hl{color:var(--orange)}
.social{display:flex;gap:14px;margin-top:8px}
.social i{width:8px;height:8px;border-radius:50%;background:#c4ccd4;display:block}
.copy{position:absolute;left:0;bottom:0;width:1200px;height:36px;border-top:1px solid #1f3a4e;display:flex;align-items:center;justify-content:center;font-size:11px;font-family:"Poppins",sans-serif}
</style>
</head>
<body>

<header class="hero">
  <div class="brand"><i></i>STEADY HARBOR</div>
  <nav class="nav"><span>HOME</span><span>ABOUT</span><span>UPCOMMING WORKSHOPS</span><span>MISSION</span><span>BLOG</span><span>CONTACT</span></nav>
  <div class="hero-word" style="top:176px">LEADERSHIP</div>
  <div class="hero-word" style="top:282px">CONSULTANT</div>
  <div class="ph hero-photo" role="img" aria-label="Portrait of Rud Calloway in a dark suit, seated in an office chair"></div>
</header>

<section class="intro">
  <h1 class="abs intro-title">I am Rud Calloway<br>Leadership Consultant</h1>
  <p class="abs intro-text">I love working with startups and the businesses looking to scale up. I'm a critical thinker and creative problem solver. I am good at presenting business ideas in a compelling and professional way.</p>
  <div class="btn btn-solid" style="left:80px;top:1058px;width:146px;height:44px">Contact Me</div>
  <div class="stats">
    <div class="stat" style="background:var(--sky)"><b>1 586</b><span>Speechs</span></div>
    <div class="stat" style="background:var(--navy)"><b>3 500</b><span>Finished Projects</span></div>
    <div class="stat" style="background:var(--amber)"><b>12</b><span>Year Experience</span></div>
    <div class="stat" style="background:var(--salmon)"><b>36</b><span>Award Winning</span></div>
  </div>
  <div class="ring" style="left:1030px;top:1040px;width:220px;height:220px;border-width:20px;border-color:var(--blue)"></div>
</section>

<section class="events">
  <div class="ring" style="left:250px;top:-30px;width:60px;height:60px;border-width:10px;border-color:var(--orange)"></div>
  <h2 class="sec-title" style="left:80px;top:96px">Upcomming Events</h2>
  <div class="arrows" style="right:80px;top:116px">
    <svg width="22" height="12" viewBox="0 0 22 12"><path d="M21 6H2M7 1L2 6l5 5" fill="none" stroke="#9aa3ad" stroke-width="1.5"/></svg>
    <svg width="22" height="12" viewBox="0 0 22 12"><path d="M1 6h19M15 1l5 5-5 5" fill="none" stroke="#9aa3ad" stroke-width="1.5"/></svg>
  </div>
  <div class="card" style="left:80px">
    <div class="ph" role="img" aria-label="Speaker in a suit standing in a bright office" style="background:linear-gradient(160deg,#c9d3dc,#3d4a5c)"><div class="date"><b>13</b><span>JUL</span></div></div>
    <div class="cap"><i></i>Unleash Your Power</div>
  </div>
  <div class="card" style="left:348px">
    <div class="ph" role="img" aria-label="Runner sprinting along a sandy track" style="background:linear-gradient(170deg,#e9e3d8,#a89a84)"><div class="date"><b>24</b><span>JUL</span></div></div>
    <div class="cap"><i></i>Be Your Own Boss</div>
  </div>
  <div class="card" style="left:612px">
    <div class="ph" role="img" aria-label="Person standing on a rocky coast looking over the sea" style="background:linear-gradient(180deg,#9fc3dc,#3f7ea6 60%,#6b5d52)"><div class="date"><b>28</b><span>JUL</span></div></div>
    <div class="cap"><i></i>Secret of Leadership</div>
  </div>
  <div class="card" style="left:872px">
    <div class="ph" role="img" aria-label="Studio portrait of a man against a dark background" style="background:linear-gradient(160deg,#3a4450,#14181e)"><div class="date"><b>07</b><span>AUG</span></div></div>
    <div class="cap"><i></i>How to Achive<br>Anything</div>
  </div>
</section>

<section class="testimonials">
  <h2 class="sec-title" style="left:80px;top:1928px">Testimonials</h2>
  <div class="arrows" style="right:80px;top:1940px">
    <svg width="22" height="12" viewBox="0 0 22 12"><path d="M21 6H2M7 1L2 6l5 5" fill="none" stroke="#9aa3ad" stroke-width="1.5"/></svg>
    <svg width="22" height="12" viewBox="0 0 22 12"><path d="M1 6h19M15 1l5 5-5 5" fill="none" stroke="#9aa3ad" stroke-width="1.5"/></svg>
  </div>
  <p class="abs quote">Chuck, thanks for the post and for mentioning the post to me. I think you cover much of this very well. In my experience with consultants, I think you reference one of the sure-fire ways to fail using consultants.</p>
  <div class="abs sans" style="left:176px;top:2172px;font-size:11px;font-weight:700">BALS</div>
  <div class="avatar" role="img" aria-label="Client portrait" style="left:176px;background:#cbb7a6"></div>
  <div class="avatar" role="img" aria-label="Client portrait" style="left:252px;background:#b9a99a;box-shadow:0 0 0 3px #fff,0 0 0 5px #e3e6ea"></div>
  <div class="avatar" role="img" aria-label="Client portrait" style="left:328px;background:#2c3036"></div>
  <div class="ring" style="left:-60px;top:1980px;width:170px;height:170px;border-width:22px;border-color:var(--orange)"></div>
  <div class="ring" style="left:560px;top:2386px;width:80px;height:80px;border-width:14px;border-color:var(--blue)"></div>
</section>

<section class="vision">
  <div class="vision-word" style="top:140px;right:-10px">VISION</div>
  <div class="vision-word" style="top:246px;right:-20px">&amp;MISSION</div>
  <h2 class="abs" style="left:80px;top:130px;font-size:40px;font-weight:600;color:var(--white)">Vision &amp; Mission</h2>
  <p class="abs vision-text">The vision statement focuses on tomorrow and what the organization wants to become. The mission statement focuses on today and what the organization does. While companies commonly use mission and vision statements interchangeably, it's important to have both.</p>
  <div class="play"><i><svg width="18" height="20" viewBox="0 0 18 20"><path d="M2 1l15 9-15 9z" fill="var(--orange)"/></svg></i><span>WATCH<br>FULL VIDEO</span></div>
  <div class="ph" role="img" aria-label="Portrait of Rud Calloway in a dark suit and striped tie" style="left:770px;top:40px;width:370px;height:620px;border-radius:170px 170px 0 0;background:linear-gradient(180deg,#d1d4da 0%,#5d6570 50%,#1f232a 100%)"></div>
</section>

<section class="news">
  <h2 class="sec-title" style="left:80px;top:3196px">Latest news</h2>
  <p class="abs" style="left:80px;top:3272px;width:260px;font-size:15px;line-height:1.6;color:var(--grey);font-weight:300">Find Coaching Classes Latest News, Videos &amp; Pictures on Coaching Classes and business motivation news</p>
  <div class="btn btn-line" style="left:80px;top:3422px;width:150px;height:44px">View More</div>
  <article class="news-card" style="left:404px">
    <div class="ph" role="img" aria-label="Team joining hands over a desk in a bright office" style="background:linear-gradient(160deg,#d9cbb6,#7a6a58)"></div>
    <div class="news-meta"><div class="news-day"><b>04</b><span>JAN 26</span></div><div><div class="news-tag">POWERMOTIVATION</div><div class="news-title">Seven Facts You Never Knew About Business.</div></div></div>
  </article>
  <article class="news-card" style="left:772px">
    <div class="ph" role="img" aria-label="Man reading a newspaper at a table" style="background:linear-gradient(160deg,#a38361,#2f241b)"></div>
    <div class="news-meta"><div class="news-day"><b>04</b><span>JAN 26</span></div><div><div class="news-tag">POWERMOTIVATION</div><div class="news-title">Looking back on 2019 + my goals for 2019</div></div></div>
  </article>
</section>

<section class="newsletter">
  <svg class="abs" style="left:80px;top:84px" width="56" height="42" viewBox="0 0 56 42"><rect x="2" y="2" width="52" height="38" rx="4" fill="none" stroke="#fff" stroke-width="3"/><path d="M3 5l25 19L53 5" fill="none" stroke="#fff" stroke-width="3"/></svg>
  <h3 class="abs" style="left:166px;top:72px;font-size:36px;font-weight:600">Newsletter</h3>
  <div class="abs sans" style="left:166px;top:122px;font-size:14px">Enter your email address &amp; get offer.</div>
  <div class="field">Email Address<div class="subscribe">Subscribe</div></div>
</section>

<footer class="footer">
  <div class="fcol" style="left:80px"><h4>Address</h4>2140 Alder Lane, Marlow<br>Springs, Ohio, 44021</div>
  <div class="fcol" style="left:350px"><h4>Contact</h4>Email: <span class="hl">hello@steadyharbor.net</span><br>Phone: 555-014-2270<div class="social"><i></i><i></i><i></i></div></div>
  <div class="fcol" style="left:630px"><h4>Navigation</h4>Home<br>About us<br>Courses</div>
  <div class="fcol" style="left:800px;top:94px">Events<br>Classes<br>Blog</div>
  <div class="fcol" style="left:966px;top:94px">Shop<br>FAQ<br>Contact</div>
  <div class="copy">All Rights Reserved by Rud Calloway</div>
</footer>

</body>
</html>
```